Create 5 images/buttons for our website (Casual beachfront Cafe/Restaurant)

Create 5 images/buttons to replace the "Buy a Gift Card", "Click Here to Book Now", "Download Breakfast Menu", "Download Lunch + Dinner Menu", "Download Takeaway Flyer", all currently on our website. Must be appropriately sized, compliment the existing website and brand (you can see photo of Cafe at www.saltmarrowcafe.com.au). Font and button shapes can be of your choice. Font colour should be either the red, blue or terracotta from our existing colour scheme. Thanks!

```html
<!DOCTYPE html>
<html lang="en">
<head>
<meta charset="utf-8">
<title>Salt Marrow Cafe – Website Buttons</title>
<link rel="stylesheet" href="https://fonts.googleapis.com/css2?family=Caveat+Brush&display=swap">
<style>
  :root {
    --bg-slate: #4a5e64;
    --sun-yellow: #ffff5a;
    --ocean-blue: #22467b;
    --terracotta: #a85a28;
    --script: "Caveat Brush", cursive;
  }
  * { box-sizing: border-box; margin: 0; padding: 0; }
  html, body { width: 853px; height: 1200px; overflow: hidden; }
  body { background: var(--bg-slate); font-family: var(--script); position: relative; }

  .brand-name {
    position: absolute; left: 231px; top: 21px; width: 419px; height: 216px;
    display: flex; align-items: center; justify-content: center; text-align: center;
    font-family: var(--script); font-weight: 400; font-size: 78px; line-height: 0.95;
    color: var(--sun-yellow);
  }

  .button {
    position: absolute; width: 258px; height: 258px; border-radius: 50%;
    background: var(--sun-yellow); text-decoration: none; overflow: hidden;
    display: flex; flex-direction: column; align-items: center; justify-content: center;
    text-align: center; line-height: 0.92;
  }
  .button::before {
    content: ""; position: absolute; inset: 10px; border-radius: 50%;
    border: 2px dotted var(--terracotta);
  }
  .button--gift     { left: 149px; top: 287px; }
  .button--book     { left: 449px; top: 287px; }
  .button--breakfast{ left: 156px; top: 591px; }
  .button--lunch    { left: 446px; top: 591px; }
  .button--takeaway { left: 295px; top: 886px; }

  .lead  { display: block; color: var(--terracotta); font-size: 34px; }
  .lead--blue { color: var(--ocean-blue); font-size: 30px; }
  .lead--small { font-size: 30px; }
  .title { display: block; color: var(--ocean-blue); font-size: 52px; }
  .title--long { font-size: 40px; }
  .title--big  { font-size: 54px; }
  .tail  { display: block; color: var(--terracotta); font-size: 32px; }
  .icon  { margin-top: 8px; fill: none; stroke: var(--ocean-blue); stroke-width: 3; stroke-linecap: round; stroke-linejoin: round; }
  .icon--tight { margin-top: 4px; }
  .download-mark { margin-bottom: 2px; fill: none; stroke: var(--terracotta); stroke-width: 3.5; stroke-linecap: round; stroke-linejoin: round; }
</style>
</head>
<body>
  <div class="brand-name">SALT MARROW<br>CAFE</div>

  <a class="button button--gift" href="#">
    <span class="lead">Buy a</span>
    <span class="title">Gift Card</span>
    <svg class="icon" width="86" height="56" viewBox="0 0 86 56" aria-hidden="true">
      <rect x="2" y="2" width="82" height="52" rx="5"/>
      <line x1="2" y1="24" x2="84" y2="24"/>
      <line x1="24" y1="2" x2="24" y2="54"/>
      <ellipse cx="18" cy="17" rx="6" ry="4"/>
      <ellipse cx="30" cy="17" rx="6" ry="4"/>
      <line x1="24" y1="22" x2="16" y2="32"/>
      <line x1="24" y1="22" x2="32" y2="32"/>
      <line x1="50" y1="36" x2="74" y2="36"/>
      <line x1="48" y1="44" x2="74" y2="44"/>
    </svg>
  </a>

  <a class="button button--book" href="#">
    <span class="lead lead--small">Click Here to</span>
    <span class="title">Book Now</span>
    <svg class="icon" width="96" height="75" viewBox="0 0 100 78" aria-hidden="true">
      <path d="M14 22 A14 14 0 1 1 38 12"/>
      <path d="M22 10 C18 4 10 10 14 16 L44 56 L30 60 C20 64 24 76 32 74 L68 76 C74 76 78 72 82 68 L96 56 C100 52 100 48 96 44 L74 20 C70 16 64 18 62 22 C58 16 52 18 50 22 C46 18 40 20 40 26 L38 28 Z"/>
    </svg>
  </a>

  <a class="button button--breakfast" href="#">
    <svg class="download-mark" width="38" height="38" viewBox="0 0 42 42" aria-hidden="true">
      <circle cx="21" cy="21" r="18"/>
      <line x1="21" y1="11" x2="21" y2="30"/>
      <polyline points="13,23 21,31 29,23"/>
    </svg>
    <span class="lead lead--small">Download</span>
    <span class="title title--long">Breakfast</span>
    <span class="tail">Menu</span>
    <svg class="icon icon--tight" width="90" height="52" viewBox="0 0 96 56" aria-hidden="true">
      <path d="M8 46 V14 C2 14 2 2 10 2 H56 C64 2 64 14 58 14 V46"/>
      <line x1="16" y1="14" x2="16" y2="46"/>
      <line x1="28" y1="22" x2="40" y2="10"/>
      <line x1="32" y1="32" x2="44" y2="20"/>
      <path d="M50 28 H76 V40 C76 46 72 48 66 48 H60 C54 48 50 46 50 40 Z"/>
      <path d="M76 31 C84 31 84 40 76 40"/>
      <path d="M60 22 V16 M66 22 V16 M72 22 V16"/>
      <rect x="2" y="48" width="92" height="6" rx="3"/>
    </svg>
  </a>

  <a class="button button--lunch" href="#">
    <svg class="download-mark" width="38" height="38" viewBox="0 0 42 42" aria-hidden="true">
      <circle cx="21" cy="21" r="18"/>
      <line x1="21" y1="11" x2="21" y2="30"/>
      <polyline points="13,23 21,31 29,23"/>
    </svg>
    <span class="lead lead--small">Download</span>
    <span class="title title--long">Lunch+Dinner</span>
    <span class="tail">Menu</span>
    <svg class="icon icon--tight" width="62" height="62" viewBox="0 0 80 80" aria-hidden="true">
      <circle cx="40" cy="44" r="34"/>
      <circle cx="40" cy="44" r="24"/>
      <path d="M22 4 V26 C22 32 34 32 34 26 V4 M28 4 V24 M28 32 V74"/>
      <path d="M52 74 V6 C60 10 62 28 60 40 H52"/>
    </svg>
  </a>

  <a class="button button--takeaway" href="#">
    <svg class="download-mark" width="38" height="38" viewBox="0 0 42 42" aria-hidden="true">
      <circle cx="21" cy="21" r="18"/>
      <line x1="21" y1="11" x2="21" y2="30"/>
      <polyline points="13,23 21,31 29,23"/>
    </svg>
    <span class="lead lead--blue">Download</span>
    <span class="title title--big">Takeaway</span>
    <span class="tail">Flyer</span>
    <svg class="icon icon--tight" width="118" height="51" viewBox="0 0 134 58" aria-hidden="true">
      <path d="M62 6 L94 2 L88 56 L56 56 Z"/>
      <path d="M94 2 L130 2 L122 54 L88 56"/>
      <rect x="68" y="12" width="14" height="16"/>
      <line x1="64" y1="36" x2="82" y2="36"/>
      <line x1="62" y1="44" x2="80" y2="44"/>
      <line x1="100" y1="14" x2="120" y2="14"/>
      <line x1="98" y1="24" x2="118" y2="24"/>
      <line x1="96" y1="34" x2="116" y2="34"/>
      <line x1="94" y1="44" x2="114" y2="44"/>
      <line x1="28" y1="8" x2="54" y2="8"/>
      <line x1="14" y1="18" x2="52" y2="18"/>
      <line x1="28" y1="28" x2="52" y2="28"/>
      <line x1="2" y1="36" x2="50" y2="36"/>
      <line x1="20" y1="44" x2="50" y2="44"/>
      <line x1="34" y1="52" x2="50" y2="52"/>
    </svg>
  </a>
</body>
</html>
```